ACCOUNTING FIRM CHRISTMAS MESSAGE AND OFFICE CLOSURE NOTIFICATION

WE WISH TO EMAIL A CHRISTMAS CARD IN EMAIL - WISHING OUR CLIENTS THE MERRY CHRISTMAS AND A SAFE, HEALTHY AND PROSPOROUS 2015. WE ALSO WOULD LIKE TO ADVISE OUR OFFICE CLOSES AT 4PM 23/12/2014 AND RE-OPENS AT 9AM ON 12TH JANUARY 2015.

Industry/Entity Type

Accounting

```html
<!DOCTYPE html>
<html lang="en">
<head>
<meta charset="utf-8">
<title>Season's Greetings – Northgate Accounting</title>
<link rel="stylesheet" href="https://fonts.googleapis.com/css2?family=Great+Vibes&family=Arimo:wght@400;700&display=swap">
<style>
  :root {
    --bg-light: #84491a;
    --bg-mid: #64340f;
    --bg-dark: #3a1c06;
    --gold: #f2a24a;
    --glow-core: #c9782a;
    --glow-mid: #9a5418;
    --script: #e8883a;
    --band: rgba(60, 26, 4, 0.55);
    --notice: #f0a656;
  }
  html, body {
    margin: 0;
    padding: 0;
    overflow: hidden;
    background: var(--bg-dark);
  }
  .card {
    position: relative;
    width: 1200px;
    height: 1069px;
    overflow: hidden;
    background:
      radial-gradient(ellipse 70% 60% at 40% 45%, var(--bg-light) 0%, var(--bg-mid) 55%, var(--bg-dark) 100%);
  }
  .brand {
    position: absolute;
    left: 66px;
    top: 118px;
    display: flex;
    align-items: center;
    gap: 14px;
    font-family: "Arimo", sans-serif;
    font-weight: 700;
    font-size: 34px;
    letter-spacing: 1px;
    color: var(--gold);
    text-transform: uppercase;
  }
  .brand-mark {
    width: 22px;
    height: 22px;
    background: var(--gold);
  }
  .tree-art {
    position: absolute;
    left: 660px;
    top: 0;
    width: 500px;
    height: 840px;
  }
  .greeting {
    position: absolute;
    inset: 0;
    font-family: "Great Vibes", cursive;
    color: var(--script);
    pointer-events: none;
  }
  .greeting-merry,
  .greeting-christmas,
  .greeting-line {
    position: absolute;
    margin: 0;
    font-weight: 400;
    line-height: 1;
    white-space: nowrap;
  }
  .greeting-merry {
    left: 426px;
    top: 446px;
    font-size: 84px;
  }
  .greeting-christmas {
    left: 262px;
    top: 502px;
    font-size: 118px;
  }
  .greeting-line-one {
    left: 313px;
    top: 640px;
    font-size: 66px;
    letter-spacing: 1px;
  }
  .greeting-line-two {
    left: 192px;
    top: 722px;
    font-size: 74px;
    letter-spacing: 3px;
  }
  .notice-band {
    position: absolute;
    left: 10px;
    right: 10px;
    top: 834px;
    height: 160px;
    background: var(--band);
    display: flex;
    align-items: center;
    justify-content: center;
  }
  .notice {
    margin: 0 0 10px;
    text-align: center;
    font-family: "Arimo", sans-serif;
    font-size: 35px;
    line-height: 44px;
    color: var(--notice);
  }
</style>
</head>
<body>
  <main class="card">
    <div class="brand">
      <span class="brand-mark"></span>
      <span class="brand-name">Northgate Accounting</span>
    </div>

    <svg class="tree-art" viewBox="0 0 500 840" role="img" aria-label="Illustration of a Christmas tree formed from glowing golden sparkles">
      <defs>
        <radialGradient id="treeGlow" cx="50%" cy="50%" r="50%">
          <stop offset="0%" stop-color="var(--glow-core)" stop-opacity="0.5"/>
          <stop offset="55%" stop-color="var(--glow-mid)" stop-opacity="0.22"/>
          <stop offset="100%" stop-color="var(--glow-mid)" stop-opacity="0"/>
        </radialGradient>
      </defs>
      <rect x="0" y="0" width="500" height="840" fill="url(#treeGlow)"/>
    </svg>

    <section class="greeting">
      <h1 class="greeting-merry">Merry</h1>
      <h1 class="greeting-christmas">Christmas</h1>
      <p class="greeting-line greeting-line-one">a safe, healthy</p>
      <p class="greeting-line greeting-line-two">and prosporous 2015</p>
    </section>

    <footer class="notice-band">
      <p class="notice">Our office closes at 4pm 23/12/2014<br>and re-opens at 9am on 12th january 2015.</p>
    </footer>
  </main>
</body>
</html>
```